business card deign

Logo needs the following on it.
1. attached logo
2. Tagline - "From frosty drinks to lively nights...we handle it all!"
3. Name- Delia Fenwick, Founder and CPO
4. Address - 418 E. Harlow Avenue, Ste 2204, Tampa, FL. 33719
5. Phone - 720.555.0187

```html
<!DOCTYPE html>
<html lang="en">
<head>
<meta charset="UTF-8">
<title>Chilloo Business Card</title>
<link href="https://fonts.googleapis.com/css2?family=Poppins:wght@400;500;600;700&display=swap" rel="stylesheet">
<style>
  :root {
    --backdrop: #3b3b3b;
    --ink: #0a0a0a;
    --paper: #ffffff;
    --muted: #4a4a4a;
    --rule: #b5b5b5;
  }
  html, body {
    margin: 0;
    padding: 0;
    width: 1200px;
    height: 689px;
    overflow: hidden;
    background: var(--backdrop);
    font-family: "Poppins", sans-serif;
  }
  .stage {
    position: relative;
    width: 1200px;
    height: 689px;
  }
  .card {
    position: absolute;
    top: 190px;
    width: 540px;
    height: 309px;
    border-radius: 18px;
    overflow: hidden;
    box-shadow: 0 14px 40px rgba(0,0,0,0.45);
  }
  .card--front { left: 40px; background: var(--ink); }
  .card--back { left: 620px; background: var(--paper); }

  .wordmark {
    display: flex;
    align-items: center;
    gap: 12px;
    font-weight: 600;
    letter-spacing: 0.35em;
  }
  .wordmark__dot {
    width: 14px;
    height: 14px;
    border-radius: 50%;
  }
  .card--front .wordmark {
    position: absolute;
    left: 0; right: 0;
    top: 100px;
    justify-content: center;
    font-size: 36px;
    color: var(--paper);
  }
  .card--front .wordmark__dot { background: var(--paper); }

  .tagline-band {
    position: absolute;
    left: 0; right: 0; bottom: 0;
    height: 62px;
    display: flex;
    align-items: center;
    justify-content: center;
    font-size: 14px;
    font-weight: 500;
  }
  .card--front .tagline-band { background: var(--paper); color: var(--ink); }
  .card--back .tagline-band { background: var(--ink); color: var(--paper); }

  .card--back .wordmark {
    position: absolute;
    left: 30px;
    top: 100px;
    width: 210px;
    justify-content: center;
    font-size: 26px;
    color: var(--ink);
  }
  .card--back .wordmark__dot { background: var(--ink); width: 11px; height: 11px; }

  .divider {
    position: absolute;
    left: 262px;
    top: 40px;
    width: 1px;
    height: 160px;
    background: var(--rule);
  }
  .contact {
    position: absolute;
    left: 286px;
    top: 44px;
    color: var(--ink);
  }
  .contact__name {
    margin: 0;
    font-size: 19px;
    font-weight: 700;
    line-height: 1.1;
    text-transform: uppercase;
  }
  .contact__role {
    margin: 2px 0 16px;
    font-size: 13px;
    color: var(--muted);
  }
  .contact__row {
    display: flex;
    align-items: flex-start;
    gap: 9px;
    font-size: 12.5px;
    line-height: 1.35;
    color: var(--muted);
    margin-bottom: 8px;
  }
  .contact__row svg { flex: none; margin-top: 2px; }
</style>
</head>
<body>
<main class="stage">
  <section class="card card--front" aria-label="Card front">
    <div class="wordmark"><span class="wordmark__dot"></span>CHILLOO</div>
    <div class="tagline-band">From frosty drinks to lively nights...we handle it all!</div>
  </section>

  <section class="card card--back" aria-label="Card back">
    <div class="wordmark"><span class="wordmark__dot"></span>CHILLOO</div>
    <div class="divider"></div>
    <div class="contact">
      <p class="contact__name">Delia Fenwick</p>
      <p class="contact__role">Founder and CPO</p>
      <div class="contact__row">
        <svg width="12" height="12" viewBox="0 0 24 24" aria-hidden="true"><path fill="#0a0a0a" d="M6.6 10.8a15.1 15.1 0 0 0 6.6 6.6l2.2-2.2a1 1 0 0 1 1-.25 11.4 11.4 0 0 0 3.6.57 1 1 0 0 1 1 1V20a1 1 0 0 1-1 1A17 17 0 0 1 3 4a1 1 0 0 1 1-1h3.5a1 1 0 0 1 1 1c0 1.25.2 2.45.57 3.57a1 1 0 0 1-.25 1z"/></svg>
        <span>720.555.0187</span>
      </div>
      <div class="contact__row">
        <svg width="12" height="14" viewBox="0 0 24 28" aria-hidden="true"><path fill="#0a0a0a" d="M12 0a9 9 0 0 0-9 9c0 6.8 9 17 9 17s9-10.2 9-17a9 9 0 0 0-9-9zm0 12.5A3.5 3.5 0 1 1 12 5.5a3.5 3.5 0 0 1 0 7z"/></svg>
        <span>418 E. Harlow Avenue,<br>Ste 2204, Tampa, FL. 33719</span>
      </div>
    </div>
    <div class="tagline-band">From frosty drinks to lively nights...we handle it all!</div>
  </section>
</main>
</body>
</html>
```